Compass of Quiet Mornings book cover design

Book cover - the book contains 52 chapters - 2 for each letter of the alphabet, so a yearlong focus on Leadership. The Intent is to communicate that leadership is common sense. It just isn’t common practice. This book allows the reader to focus on one leadership word each week for a yearlong focus on improving one’s leadership. It is full of stories relating to the 52 words that will challenge and inspire the reader.
Target Market(s)
Leaders / Emerging Leaders
Industry/Entity Type
All
Requirements
Must have
- Appeal to executives
Nice to have
- Simplicity
Should not have
- Cartoon feel

```html
<!DOCTYPE html>
<html lang="en">
<head>
<meta charset="UTF-8">
<title>Compass of Quiet Mornings – Book Cover</title>
<link rel="stylesheet" href="https://fonts.googleapis.com/css2?family=Bebas+Neue&family=Open+Sans:wght@400&display=swap">
<style>
  :root {
    --backdrop: #e6cd93;
    --cover-dark: #121518;
    --teal: #0b8c80;
    --title-grey: #d6d8da;
    --tag-white: #e8eaeb;
    --photo-blue: #3d7394;
    --photo-deep: #1b2e3b;
  }
  * { margin: 0; padding: 0; box-sizing: border-box; }
  html, body {
    width: 1200px; height: 857px; overflow: hidden;
    background: var(--backdrop);
  }
  .canvas { position: relative; width: 1200px; height: 857px; }
  .cover {
    position: absolute; left: 320px; top: 28px;
    width: 560px; height: 800px;
    background: var(--cover-dark);
    overflow: hidden;
  }
  .author-photo {
    position: absolute; left: 0; top: 0;
    width: 340px; height: 800px;
    background:
      linear-gradient(90deg, rgba(18,21,24,0) 55%, var(--cover-dark) 100%),
      linear-gradient(180deg, var(--photo-deep) 0%, var(--photo-blue) 35%, #2c5670 60%, #151d24 100%);
  }
  .author-name {
    position: absolute; right: 44px; top: 92px;
    font-family: "Bebas Neue", sans-serif;
    font-weight: 400;
    font-size: 80px; line-height: 72px;
    color: var(--teal);
    text-align: right;
  }
  .title {
    position: absolute; right: 44px; top: 400px;
    font-family: "Bebas Neue", sans-serif;
    font-weight: 400;
    color: var(--title-grey);
    text-align: right;
  }
  .title-main { display: block; font-size: 112px; line-height: 96px; }
  .title-row { display: flex; align-items: center; justify-content: flex-end; gap: 12px; }
  .title-small {
    font-family: "Open Sans", sans-serif;
    font-weight: 400;
    font-size: 20px;
    margin-top: -18px;
  }
  .tagline {
    position: absolute; right: 44px; top: 610px;
    font-family: "Open Sans", sans-serif;
    font-size: 15px; line-height: 21px;
    color: var(--tag-white);
    text-align: right;
  }
  .tagline .accent { color: var(--teal); }
</style>
</head>
<body>
<div class="canvas">
  <section class="cover">
    <div class="author-photo" role="img" aria-label="Blue-toned portrait of the author resting his chin on his hand"></div>
    <h2 class="author-name">Daniel<br>Whitcombe</h2>
    <h1 class="title">
      <span class="title-main">Compass</span>
      <span class="title-row"><span class="title-small">of quiet</span><span class="title-main">Mornings</span></span>
    </h1>
    <p class="tagline">Not just COMMON Practive.<br>It is <span class="accent">COMMON SENSE</span>.</p>
  </section>
</div>
</body>
</html>
```